Inflatable Movie Screen company needs a Brochure Design for sales kit

We need a brochure as per attached sketch drawing which is to:
1)follow the sample layout
2) attached images must be used
3) to follow company corporate colors or suggest something professional and appropriate for the theme
Updates

Target Market(s)

Corporate and Community Clubs

Industry/Entity Type

Entertainment

Requirements
Must have
• Colors to be in line with corporate colors OR to suggest something appropriate.
Nice to have
• A unique concept
Should not have
• Too fanciful

```html
<!DOCTYPE html>
<html lang="en">
<head>
<meta charset="utf-8">
<title>Lumora Inflatable Movie Screening Flyer</title>
<link href="https://fonts.googleapis.com/css2?family=Cinzel:wght@400;500&family=Montserrat:wght@300;400;600;700&display=swap" rel="stylesheet">
<style>
  :root {
    --page: #e9e9ea;
    --paper: #ffffff;
    --navy: #0f2f4a;
    --navy-mid: #1d4d6e;
    --navy-light: #2f6d8c;
    --slate: #8e8f93;
    --title-box: rgba(138, 139, 143, 0.9);
    --teal: #1fbfc4;
    --teal-deep: #17a6ab;
    --ink: #2b2b2b;
    --footer-bar: #34495a;
  }
  * { margin: 0; padding: 0; box-sizing: border-box; }
  html, body { width: 1198px; height: 1200px; overflow: hidden; background: var(--page); }
  .flyer {
    position: absolute; left: 135px; top: 0;
    width: 927px; height: 1200px;
    background: var(--paper); overflow: hidden;
  }
  .artwork { position: absolute; left: 0; top: 0; }
  .title-box {
    position: absolute; left: 0; top: 35px; width: 537px; height: 281px;
    background: var(--title-box); color: #fff;
    font-family: 'Cinzel', serif;
  }
  .title-line { position: absolute; white-space: nowrap; line-height: 1; }
  .title-kicker { left: 44px; top: 50px; font-size: 42px; }
  .title-main { left: 28px; top: 84px; font-size: 127px; letter-spacing: -2px; }
  .title-sub { left: 130px; top: 218px; font-size: 58px; letter-spacing: -1px; }
  .title-sub .title-by { font-size: 38px; letter-spacing: 0; margin-left: 6px; }
  .brand-box {
    position: absolute; left: 537px; top: 106px; width: 390px; height: 135px;
    background: var(--title-box); color: #fff; text-align: center;
    font-family: 'Cinzel', serif;
  }
  .brand-name { display: block; margin-top: 18px; font-size: 66px; line-height: 1; }
  .brand-legal { display: block; margin-top: 8px; font-size: 13px; letter-spacing: 1px; }
  .testimonial {
    position: absolute; left: 54px; top: 908px; width: 400px;
    font-family: 'Montserrat', sans-serif; font-weight: 300;
    font-size: 19px; line-height: 34px; color: var(--ink);
  }
  .testimonial-author { font-weight: 600; }
  .quote-mark {
    position: absolute; font-family: 'Montserrat', sans-serif; font-weight: 700;
    color: var(--slate); font-size: 90px; line-height: 1;
  }
  .quote-open { left: 50px; top: 858px; }
  .quote-close { left: 262px; top: 1036px; }
  .feature-quote {
    position: absolute; right: 45px; top: 880px; width: 360px; text-align: right;
    font-family: 'Montserrat', sans-serif; font-weight: 300;
    font-size: 19px; line-height: 34px; color: var(--ink);
  }
  .feature-author {
    position: absolute; right: 45px; top: 1090px;
    font-family: 'Montserrat', sans-serif; font-weight: 600; font-size: 19px; color: var(--ink);
  }
  .website {
    position: absolute; left: 74px; top: 1148px;
    font-family: 'Montserrat', sans-serif; font-weight: 700;
    font-size: 12px; letter-spacing: 2.5px; color: var(--footer-bar);
  }
  .footer-bar { position: absolute; left: 602px; top: 1179px; width: 325px; height: 21px; background: var(--footer-bar); }
</style>
</head>
<body>
<main class="flyer">
  <svg class="artwork" width="927" height="1200" viewBox="0 0 927 1200">
    <defs>
      <clipPath id="main-photo-clip"><circle cx="600" cy="360" r="412"/></clipPath>
      <clipPath id="inset-photo-clip"><circle cx="258" cy="621" r="151"/></clipPath>
      <linearGradient id="dusk-lawn" x1="0" y1="0" x2="0" y2="1">
        <stop offset="0" stop-color="#dfe6ee"/>
        <stop offset="0.45" stop-color="#b9c2c8"/>
        <stop offset="0.6" stop-color="#6c7a5c"/>
        <stop offset="1" stop-color="#4e6a3e"/>
      </linearGradient>
      <linearGradient id="night-lawn" x1="0" y1="0" x2="0" y2="1">
        <stop offset="0" stop-color="#1e2a2c"/>
        <stop offset="0.5" stop-color="#2c3b36"/>
        <stop offset="1" stop-color="#3b4b3a"/>
      </linearGradient>
    </defs>

    <g class="dark-facets">
      <polygon points="0,0 380,0 210,320 28,716 0,690" fill="var(--navy)"/>
      <polygon points="0,0 150,0 0,260" fill="var(--navy-mid)"/>
      <polygon points="60,380 210,320 28,716" fill="var(--navy-light)" opacity="0.55"/>
      <polygon points="0,420 60,380 28,716 0,690" fill="var(--navy-mid)" opacity="0.7"/>
    </g>

    <g clip-path="url(#main-photo-clip)">
      <rect class="main-photo" x="150" y="-60" width="780" height="900" fill="url(#dusk-lawn)"
            role="img" aria-label="Photo: families seated on a lawn at dusk watching a large inflatable outdoor movie screen"/>
    </g>

    <circle class="slate-ring" cx="600" cy="360" r="450" fill="none" stroke="var(--slate)" stroke-width="76"/>
    <path class="teal-arc" d="M145 622 A525 525 0 0 0 627 884" fill="none" stroke="var(--teal)" stroke-width="56"/>

    <circle class="inset-frame" cx="258" cy="621" r="165" fill="var(--teal)"/>
    <g clip-path="url(#inset-photo-clip)">
      <rect class="inset-photo" x="100" y="465" width="320" height="320" fill="url(#night-lawn)"
            role="img" aria-label="Photo: evening crowd on a field watching a film on an inflatable screen"/>
    </g>
  </svg>

  <header class="title-box">
    <span class="title-line title-kicker">Inflatable</span>
    <span class="title-line title-main">MOVIE</span>
    <span class="title-line title-sub">SCREENING<span class="title-by">BY</span></span>
  </header>

  <div class="brand-box">
    <span class="brand-name">LUMORA</span>
    <span class="brand-legal">LUMORA EVENTS PTE LTD</span>
  </div>

  <span class="quote-mark quote-open">&ldquo;</span>
  <blockquote class="testimonial">
    Enjoyed watching movie name 7 with<br>
    my family. It was nice to get away from<br>
    the usual malls and bond together.<br>
    My kids loved it!<br>
    <span class="testimonial-author">-May Tan, Housewife</span>
  </blockquote>
  <span class="quote-mark quote-close">&rdquo;</span>

  <blockquote class="feature-quote">
    &ldquo;Of all our inventionsfor<br>
    mass communications,<br>
    pictures still speak the<br>
    most universally<br>
    understood language.&rdquo;
  </blockquote>
  <p class="feature-author">- Arthur Penrose</p>

  <p class="website">WWW.LUMORAEVENTS.COM</p>
  <div class="footer-bar"></div>
</main>
</body>
</html>
```